Cards and what not
Project: Stationary
Stationary - Consulting
Stationary
Simple
Tomaso Reyk Halden
CEO
Do not want to use an address please.
833-LUMACORP (833-586-2267)
th@lumacorp.com
www.lumacorp.com
Please make the font large enough to more easily read. Some cards...the font is too small. Please use our logo as well. I prefer a vertical design but open to horizontal too. Many thanks :)
lumacorp lumacorp
I am looking for a vertical design while open to checking out horizontal designs (for the business card). Thanks guys (and ladies)

```html
<!DOCTYPE html>
<html lang="en">
<head>
<meta charset="utf-8">
<title>Lumacorp Business Card</title>
<link rel="stylesheet" href="https://fonts.googleapis.com/css2?family=Cinzel:wght@500&family=Montserrat:wght@400;500;600&display=swap">
<style>
  :root {
    --backdrop: #8f9193;
    --card: #ffffff;
    --brand-blue: #2fb7e6;
    --brand-teal: #3aa6c6;
    --band-grey: #c4c7ca;
    --band-grey-dark: #a9adb1;
    --ink: #3b3d40;
    --ink-soft: #5f6267;
  }
  * { box-sizing: border-box; margin: 0; padding: 0; }
  html, body { width: 1200px; height: 895px; overflow: hidden; }
  body {
    background: var(--backdrop);
    font-family: "Montserrat", sans-serif;
    color: var(--ink);
    position: relative;
  }
  .card {
    position: absolute;
    left: 270px;
    width: 660px;
    height: 377px;
    background: var(--card);
    overflow: hidden;
  }
  .card--front { top: 50px; }
  .card--back { top: 468px; }
  .band { position: absolute; left: 0; width: 100%; }
  .band--top { top: 0; }
  .band--bottom { bottom: 0; }

  .brand {
    position: absolute;
    color: var(--brand-teal);
  }
  .brand__name {
    font-family: "Cinzel", serif;
    font-weight: 500;
    letter-spacing: 2px;
    line-height: 1;
  }
  .brand__tagline {
    text-transform: uppercase;
    color: var(--ink-soft);
    font-weight: 500;
  }
  .card--front .brand { left: 0; right: 0; top: 150px; text-align: center; }
  .card--front .brand__name { font-size: 54px; }
  .card--front .brand__tagline { font-size: 13px; letter-spacing: 2.5px; margin-top: 10px; }

  .card--back .brand { left: 44px; top: 56px; text-align: left; }
  .card--back .brand__name { font-size: 34px; }
  .card--back .brand__tagline { font-size: 11px; letter-spacing: 1.5px; margin-top: 6px; }

  .person { position: absolute; right: 44px; top: 120px; text-align: right; }
  .person__name { font-size: 21px; font-weight: 500; letter-spacing: 1px; text-transform: uppercase; }
  .person__role { font-size: 13px; font-weight: 500; letter-spacing: 1.5px; text-transform: uppercase; color: var(--ink-soft); margin-top: 4px; }

  .info-strip { position: absolute; left: 0; top: 172px; }

  .contact-col {
    position: absolute;
    top: 244px;
    font-size: 15px;
    line-height: 1.6;
    color: var(--ink);
  }
  .contact-col--email { left: 40px; }
  .contact-col--web { left: 262px; }
  .contact-col--phone { left: 484px; }
</style>
</head>
<body>

<section class="card card--front" aria-label="Card front">
  <svg class="band band--top" width="660" height="52" viewBox="0 0 660 52">
    <rect width="660" height="44" fill="var(--brand-blue)"/>
    <polygon points="0,44 180,44 196,52 0,52" fill="var(--brand-blue)"/>
    <polygon points="180,44 196,30 212,44 196,52" fill="var(--band-grey)"/>
    <polygon points="448,44 464,30 480,44 464,52" fill="var(--band-grey)"/>
    <polygon points="480,44 660,44 660,52 464,52" fill="var(--brand-blue)"/>
  </svg>
  <div class="brand">
    <div class="brand__name">lumacorp</div>
    <div class="brand__tagline">Strategy and consulting services</div>
  </div>
  <svg class="band band--bottom" width="660" height="52" viewBox="0 0 660 52">
    <rect y="8" width="660" height="44" fill="var(--brand-blue)"/>
    <polygon points="180,8 196,22 212,8 196,0" fill="var(--band-grey)"/>
    <polygon points="448,8 464,22 480,8 464,0" fill="var(--band-grey)"/>
  </svg>
</section>

<section class="card card--back" aria-label="Card back">
  <svg class="band band--top" width="660" height="30" viewBox="0 0 660 30">
    <rect width="660" height="30" fill="var(--brand-blue)"/>
  </svg>
  <div class="brand">
    <div class="brand__name">lumacorp</div>
    <div class="brand__tagline">Strategy and consulting services</div>
  </div>
  <div class="person">
    <div class="person__name">Tomaso Reyk Halden</div>
    <div class="person__role">CEO</div>
  </div>

  <svg class="info-strip" width="660" height="56" viewBox="0 0 660 56">
    <rect width="660" height="56" fill="var(--band-grey)"/>
    <rect x="222" width="222" height="56" fill="var(--band-grey-dark)" opacity="0.45"/>
    <polyline points="222,0 240,28 222,56" fill="none" stroke="#fff" stroke-width="3"/>
    <polyline points="444,0 462,28 444,56" fill="none" stroke="#fff" stroke-width="3"/>
    <g class="icon-mail" fill="none" stroke="#fff" stroke-width="2">
      <rect x="42" y="18" width="28" height="20" rx="2"/>
      <polyline points="42,19 56,30 70,19"/>
    </g>
    <g class="icon-globe" fill="none" stroke="#fff" stroke-width="2">
      <circle cx="300" cy="28" r="12"/>
      <ellipse cx="300" cy="28" rx="5" ry="12"/>
      <line x1="288" y1="28" x2="312" y2="28"/>
      <line x1="290" y1="21" x2="310" y2="21"/>
      <line x1="290" y1="35" x2="310" y2="35"/>
    </g>
    <g class="icon-phone">
      <rect x="513" y="13" width="16" height="30" rx="3" fill="none" stroke="#fff" stroke-width="2"/>
      <line x1="518" y1="38" x2="524" y2="38" stroke="#fff" stroke-width="2"/>
    </g>
  </svg>

  <div class="contact-col contact-col--email">th@lumacorp.com</div>
  <div class="contact-col contact-col--web">www.lumacorp.com</div>
  <div class="contact-col contact-col--phone">
    833-LUMACORP<br>833-586-2267
  </div>

  <svg class="band band--bottom" width="660" height="30" viewBox="0 0 660 30">
    <rect width="660" height="30" fill="var(--brand-blue)"/>
  </svg>
</section>

</body>
</html>
```